verdant terraces simple classy business card design

my name is owen harlow and I run a gardening business aimed at high class verdant terraces. the business name is verdant terraces and our logo was designed on pixel forum .My clientel are anything from residential homes to businesses. I take pride in my work and know that I offer a service like no other in my area.
The business card will be used to represent my business and I want it to be not only rememberable, but simplistic and modern. Eye catching too. Of course I would like it relatable to gardening and appealing to the correct clientel - those being garden enthusiasts, prestigious homes and businesses that are after top of the line gardening services like no other on the market.
I am not a typical lawn mowing business so I don't want a typical card design that represents that. The gardens I work with are generally million dollar properties with owners who are very garden proud looking for upkeep and guidance from me along with sometimes whole new garden designs. I want the business cards to show to my clients that I take pride, as they do, in their garden. And I want them to know from my card that I am a professional, qualified horticulturist offering them a top of the line service for life. I want them to refer my business on. I want them to look at my business card and see class and professionalism in a modern unique bold way.
The card should be simple with the possibility of the logo on the front being embossed/debossed and my details on the back the card should have a organic garden feel it's very important to me that it is absolutely perfect
I am also very open to ideas and suggestions so look forward to seeing the designs. the business logo has been supplied with this project and I want the card to be double sided

Contact info is
Owen Harlow - Managing Director / Horticulturist
Phone : 0481 526 704
Email: owenharlow@verdantterraces.com.au

Target Market(s)

high class gardens residential and commercial

Industry/Entity Type

Gardener

Contact Information for Business Card

Contact info is
Phone : 0481 526 704

PLEASE MAKE CARD DOUBLE SIDED

Requirements
Must have
• organic simple classy modern feel
• must flow with the current logo that has been supplied with this project
• Double sided
• Must explain in a simple way that I deal with high end gardens and I'm a qualified horticulturist
Nice to have
• embossed debossed logo
Should not have
• shouldn't be to busy or cheap looking

```html
<!DOCTYPE html>
<html lang="en">
<head>
<meta charset="utf-8">
<title>Verdant Terraces – Business Card</title>
<link rel="stylesheet" href="https://fonts.googleapis.com/css2?family=Montserrat:wght@400;600&display=swap">
<style>
  :root {
    --backdrop: #2b2b2b;
    --leaf-green: #5e9e5b;
    --card-white: #ebebeb;
    --ink-white: #ffffff;
    --emboss-grey: #c6c6c6;
  }
  * { margin: 0; padding: 0; box-sizing: border-box; }
  html, body {
    width: 1200px; height: 900px; overflow: hidden;
    background: var(--backdrop);
    font-family: "Montserrat", sans-serif;
  }
  .canvas { position: relative; width: 1200px; height: 900px; }
  .card {
    position: absolute; left: 250px; width: 700px; height: 400px;
    border-radius: 26px; overflow: hidden;
  }
  .card-front { top: 35px; background: var(--leaf-green); }
  .card-back { top: 465px; background: var(--card-white); }

  .front-brand {
    position: absolute; inset: 0;
    display: flex; flex-direction: column; align-items: center; justify-content: center; gap: 18px;
    color: var(--ink-white);
    font-weight: 400; font-size: 30px; letter-spacing: 6px; text-transform: uppercase;
  }
  .front-brand .brand-dot {
    width: 110px; height: 110px; border-radius: 50%; background: var(--ink-white);
  }

  .back-brand {
    position: absolute; left: 40px; top: 150px;
    color: var(--emboss-grey);
    font-weight: 400; font-size: 28px; letter-spacing: 5px; text-transform: uppercase;
    line-height: 1.5;
  }

  .contact-panel { position: absolute; inset: 0; }

  .contact-details {
    position: absolute; right: 30px; top: 172px;
    text-align: right; color: var(--ink-white);
  }
  .contact-name { font-weight: 600; font-size: 26px; line-height: 32px; margin-bottom: 6px; }
  .contact-role { font-weight: 400; font-size: 13.5px; line-height: 18px; margin-bottom: 14px; }
  .contact-line {
    display: flex; justify-content: flex-end; align-items: center; gap: 8px;
    font-size: 13.5px; line-height: 18px; margin-bottom: 12px;
  }
  .contact-line svg { width: 12px; height: 12px; }
</style>
</head>
<body>
<div class="canvas">

  <section class="card card-front">
    <div class="front-brand">
      <span class="brand-dot"></span>
      <span class="brand-name">Verdant Terraces</span>
    </div>
  </section>

  <section class="card card-back">
    <div class="back-brand">Verdant<br>Terraces</div>

    <svg class="contact-panel" viewBox="0 0 700 400" width="700" height="400">
      <polygon points="340,400 340,190 700,95 700,400" fill="var(--leaf-green)"/>
      <polygon points="350,400 350,197 700,105 700,400" fill="var(--card-white)"/>
      <polygon points="358,386 358,204 700,114 700,386" fill="var(--leaf-green)"/>
    </svg>

    <div class="contact-details">
      <p class="contact-name">Owen Harlow</p>
      <p class="contact-role">Managing Director / Horticulturist</p>
      <p class="contact-line">0481 526 704
        <svg viewBox="0 0 24 24" aria-hidden="true"><path fill="#fff" d="M6.6 10.8a15 15 0 0 0 6.6 6.6l2.2-2.2c.3-.3.7-.4 1-.2 1.1.4 2.3.6 3.6.6.6 0 1 .4 1 1V20c0 .6-.4 1-1 1A17 17 0 0 1 3 4c0-.6.4-1 1-1h3.5c.6 0 1 .4 1 1 0 1.3.2 2.5.6 3.6.1.3 0 .7-.2 1z"/></svg>
      </p>
      <p class="contact-line">owenharlow@verdantterraces.com.au
        <svg viewBox="0 0 24 24" aria-hidden="true"><rect x="2" y="5" width="20" height="14" rx="2" fill="none" stroke="#fff" stroke-width="2"/><path d="M3 6l9 7 9-7" fill="none" stroke="#fff" stroke-width="2"/></svg>
      </p>
    </div>
  </section>

</div>
</body>
</html>
```